UI Graphics Design For Web Based Home Control

Hi,
Our company Brell Systems is looking for user interface graphics in form of *.psd for home control user interface for a real system which can be used on mobile and PC/MAC.
In Ideal solution, the same interface should be used on mobile, tablets, computers. It changes only to fit the size of the screen. The bigger the screen, the more options you have visible on same view. The user should get familiar interface logic with every device.
The design should have at least the following views covered:
1. Lights view
- List of rooms and lamps
- You can see the status and you can switch it on/off
2. Login view
- Logo (company logo attached)
- Username field
- Password field
3. Dashboard view
- Indicating and choosing home/not home
- Can go to lights view
- Can go to settings view
- Notification list
4. Settings view
- View and edit users
- View and edit lights
Show us your view of ideal home control UI :)
Updates
Time of the project extended by 10 days to receive more designs. If someone sees that the reward should be increased, please also provide the amount expected with the first design. We are willing to increase the amount paid if we see a good design.
Reason: We expect to receive more designs. We are willing to increase the reward if we see good and acceptable designs. Please provide the amount expected with the first design. Project will end with full designs available.
We added our input as an attachment how we see the UI logic. Please have a look into the file.
Reason: We are seeing some good designs. We increased the budget. We are still not where we expect.

```html
<!DOCTYPE html>
<html lang="en">
<head>
<meta charset="utf-8">
<title>Brell Systems – Home Control UI Kit</title>
<link href="https://fonts.googleapis.com/css2?family=Roboto:wght@300;400;500&display=swap" rel="stylesheet">
<style>
:root{
  --page:#f2f2f2;
  --panel-top:#4a4e57;
  --panel-bottom:#30333a;
  --text:#e4e6ea;
  --muted:#8c919a;
  --faint:#6c727c;
  --blue:#1a8fd6;
  --blue-deep:#0d5aa7;
  --glow:#58bcff;
  --green:#3fb34f;
  --field:#f7f7f7;
  --light-row-top:#e9eef2;
  --light-row-bottom:#b9c3cb;
  --heading:#858585;
}
*{box-sizing:border-box;margin:0;padding:0}
html,body{width:1200px;height:1128px;overflow:hidden}
body{background:var(--page);font-family:"Roboto",Arial,sans-serif;position:relative;color:var(--text)}
.abs{position:absolute}
.section-title{position:absolute;color:var(--heading);font-size:23px;font-weight:400;letter-spacing:.5px}
.panel{position:absolute;background:linear-gradient(var(--panel-top),var(--panel-bottom));border-radius:12px;box-shadow:0 5px 10px rgba(0,0,0,.35)}
.glow{position:absolute;left:0;right:0;height:2px;background:linear-gradient(90deg,transparent,var(--glow) 50%,transparent)}
.sep{position:absolute;left:0;right:0;height:1px;background:#24262b;border-bottom:1px solid #565b64}
.vsep{position:absolute;width:1px;background:#24262b;border-right:1px solid #565b64}
.brand{position:absolute;left:0;right:0;text-align:center;font-weight:400;letter-spacing:2px;color:#e8e8e8}
.ico{position:absolute;color:#d8dbe0}
.field{position:absolute;background:var(--field);border-radius:2px;color:#6a6e75;font-size:11px;display:flex;align-items:center}
.label{position:absolute;font-size:11px;color:var(--muted)}
.radio{position:absolute;font-size:9px;color:#b9bdc4;display:flex;align-items:center;gap:6px}
.radio::before{content:"";width:6px;height:6px;border-radius:50%;background:#fff;box-shadow:0 0 0 1.5px #8fcfff}
.btn{position:absolute;background:linear-gradient(#f8f9fa,#c9d0d6);color:var(--blue-deep);font-size:12px;text-align:center;border-radius:2px;box-shadow:0 2px 3px rgba(0,0,0,.4)}
.btn::before{content:"";position:absolute;left:-6px;right:-6px;top:-2px;height:2px;background:linear-gradient(90deg,transparent,var(--glow),transparent)}
.small{position:absolute;left:0;right:0;text-align:center;font-size:8px;color:var(--faint)}
.lorem{position:absolute;text-align:center;font-size:7px;line-height:9px;color:#9da2aa}
.toggle{position:absolute;height:14px;border-radius:7px;background:linear-gradient(#d4d7db,#9ea3a9)}
.toggle .fill{position:absolute;left:0;top:0;bottom:0;border-radius:7px;background:linear-gradient(#55c0ff,#0f78c4)}
.toggle .knob{position:absolute;top:-7px;width:28px;height:28px;border-radius:50%;background:radial-gradient(#6b7078,#3a3d44);border:2px solid #d9dce0;box-shadow:0 2px 4px rgba(0,0,0,.5)}
.toggle .knob svg{position:absolute;left:5px;top:5px}
.cap{position:absolute;font-size:11px;color:#d0d3d8}
.cell-label{position:absolute;left:0;right:0;text-align:center;font-size:19px;font-weight:300;color:var(--text)}
.row-label{position:absolute;left:82px;font-size:19px;font-weight:300;color:var(--text)}
.row-active{position:absolute;left:0;right:0;background:linear-gradient(var(--light-row-top),var(--light-row-bottom))}
.menu-item{position:absolute;left:0;right:0;text-align:center;font-size:19px;color:var(--blue-deep)}
</style>
</head>
<body>

<svg width="0" height="0" style="position:absolute">
  <defs>
    <symbol id="i-gear" viewBox="0 0 24 24"><circle cx="12" cy="12" r="7.5" fill="none" stroke="currentColor" stroke-width="4" stroke-dasharray="2.6 2.3"/><circle cx="12" cy="12" r="6" fill="none" stroke="currentColor" stroke-width="2.2"/></symbol>
    <symbol id="i-house" viewBox="0 0 24 24"><path d="M2 12.5 12 3l10 9.5h-3V21h-5v-5h-4v5H5v-8.5z" fill="currentColor"/></symbol>
    <symbol id="i-door" viewBox="0 0 24 24"><path d="M9 3h11v18H9z" fill="none" stroke="currentColor" stroke-width="1.6"/><path d="M9 3l7 2v16l-7-0z" fill="currentColor" opacity=".8"/><path d="M2 12h6m-2.5-2.5L8 12l-2.5 2.5" fill="none" stroke="currentColor" stroke-width="1.6"/></symbol>
    <symbol id="i-shield" viewBox="0 0 24 24"><path d="M12 2l8.5 3v6c0 5.5-3.8 9.2-8.5 11-4.7-1.8-8.5-5.5-8.5-11V5z" fill="none" stroke="currentColor" stroke-width="1.8"/><path d="M12 5l6 2.2v3.8L7 17c-.9-1.6-1-3.5-1-6V7.2z" fill="currentColor" opacity=".85"/></symbol>
    <symbol id="i-compass" viewBox="0 0 24 24"><circle cx="12" cy="12" r="9.5" fill="none" stroke="currentColor" stroke-width="1.6"/><path d="M8 16l8-8" stroke="currentColor" stroke-width="1.8"/></symbol>
    <symbol id="i-monitor" viewBox="0 0 24 24"><rect x="2.5" y="4" width="19" height="12.5" rx="1" fill="none" stroke="currentColor" stroke-width="1.6"/><rect x="4.5" y="6" width="15" height="8.5" fill="currentColor" opacity=".3"/><path d="M10 17v2.5H7.5h9H14V17" fill="none" stroke="currentColor" stroke-width="1.6"/></symbol>
    <symbol id="i-pen" viewBox="0 0 24 24"><path d="M4 4l13 13 1.5 4-4-1.5L1.5 6.5z" fill="none" stroke="currentColor" stroke-width="1.6"/><path d="M3 21h18" stroke="currentColor" stroke-width="1.4"/></symbol>
    <symbol id="i-bulb" viewBox="0 0 24 24"><path d="M12 2a6.5 6.5 0 0 0-4 11.6V17h8v-3.4A6.5 6.5 0 0 0 12 2z" fill="currentColor"/><rect x="8.5" y="18" width="7" height="2" fill="currentColor"/><rect x="10" y="21" width="4" height="1.5" fill="currentColor"/></symbol>
    <symbol id="i-user" viewBox="0 0 24 24"><circle cx="12" cy="8" r="4.5" fill="none" stroke="currentColor" stroke-width="1.6"/><path d="M3 21c1-5 4.5-7 9-7s8 2 9 7z" fill="none" stroke="currentColor" stroke-width="1.6"/></symbol>
    <symbol id="i-user-solid" viewBox="0 0 24 24"><circle cx="12" cy="7.5" r="4.5" fill="currentColor"/><path d="M3 21c1-5 4.5-7.5 9-7.5s8 2.5 9 7.5z" fill="currentColor"/></symbol>
    <symbol id="i-lock" viewBox="0 0 24 24"><path d="M8 10V7a4 4 0 0 1 8 0v3" fill="none" stroke="currentColor" stroke-width="2"/><rect x="5" y="10" width="14" height="11" rx="1" fill="currentColor"/></symbol>
    <symbol id="i-mail" viewBox="0 0 24 24"><rect x="2.5" y="5" width="19" height="14" fill="none" stroke="currentColor" stroke-width="1.6"/><path d="M2.5 5l9.5 8 9.5-8M2.5 19l7-7m12 7l-7-7" fill="none" stroke="currentColor" stroke-width="1.4"/></symbol>
    <symbol id="i-card" viewBox="0 0 24 24"><rect x="2.5" y="6" width="19" height="14" rx="1" fill="none" stroke="currentColor" stroke-width="1.6"/><rect x="9" y="3" width="6" height="4" fill="none" stroke="currentColor" stroke-width="1.4"/><circle cx="8" cy="12" r="2" fill="currentColor"/><path d="M5 17c.5-2 1.5-2.6 3-2.6s2.5.6 3 2.6z" fill="currentColor"/><path d="M13 11h6M13 14h6M13 17h4" stroke="currentColor" stroke-width="1.3"/></symbol>
    <symbol id="i-chev-right" viewBox="0 0 24 24"><path d="M9 5l7 7-7 7" fill="none" stroke="currentColor" stroke-width="2.4"/></symbol>
    <symbol id="i-chev-left" viewBox="0 0 24 24"><path d="M15 5l-7 7 7 7" fill="none" stroke="currentColor" stroke-width="2.4"/></symbol>
    <symbol id="i-chat" viewBox="0 0 24 24"><ellipse cx="12" cy="11" rx="10" ry="7.5" fill="currentColor"/><path d="M5 16l-2 5 6-3z" fill="currentColor"/></symbol>
    <symbol id="i-search" viewBox="0 0 24 24"><circle cx="14" cy="10" r="6" fill="none" stroke="currentColor" stroke-width="2.2"/><path d="M9.5 14.5L3.5 20.5" stroke="currentColor" stroke-width="2.6"/></symbol>
  </defs>
</svg>

<!-- Section heading -->
<div class="section-title" style="left:52px;top:48px">DARK OPTION</div>

<!-- Login view -->
<section class="panel login" style="left:38px;top:107px;width:212px;height:264px">
  <div class="brand" style="top:14px;font-size:19px">BRELL SYSTEMS</div>
  <div class="glow" style="top:50px"></div>
  <div class="label" style="left:26px;top:62px">Username</div>
  <div class="field" style="left:8px;top:78px;width:197px;height:27px">
    <svg class="ico" style="left:8px;top:4px;color:#3c3f45" width="19" height="19"><use href="#i-user-solid"/></svg>
    <span style="margin-left:72px;color:#8a8e95">brell_user</span>
  </div>
  <div class="label" style="left:26px;top:116px">Password</div>
  <div class="field" style="left:8px;top:133px;width:197px;height:27px">
    <svg class="ico" style="left:8px;top:4px;color:#3c3f45" width="17" height="19"><use href="#i-lock"/></svg>
    <span style="margin-left:66px;color:#8a8e95;font-size:7px;letter-spacing:1px">••••••••••••••••••••</span>
  </div>
  <div class="radio" style="left:12px;top:173px;font-size:11px">Save my Info</div>
  <div class="btn" style="left:68px;top:199px;width:93px;height:25px;line-height:25px">Login</div>
  <div class="small" style="top:232px">Lost your password?</div>
  <div class="small" style="top:244px">Not a member?</div>
</section>

<!-- Register view -->
<section class="panel register" style="left:300px;top:67px;width:224px;height:368px">
  <div class="brand" style="top:16px;font-size:22px">BRELL SYSTEMS</div>
  <div class="glow" style="top:70px"></div>
  <div class="brand" style="top:84px;font-size:13px;letter-spacing:.5px">REGISTER NOW</div>
  <div class="field" style="left:15px;top:113px;width:193px;height:28px;padding-left:18px">Username</div>
  <div class="field" style="left:15px;top:158px;width:193px;height:28px;padding-left:18px">First Name</div>
  <div class="field" style="left:15px;top:198px;width:193px;height:28px;padding-left:18px">Second Name</div>
  <div class="field" style="left:15px;top:236px;width:193px;height:28px;padding-left:18px">Password</div>
  <div class="radio" style="left:18px;top:274px">Accept term and conditions</div>
  <div class="radio" style="left:18px;top:287px">I want to receive news and Promotions</div>
  <div class="btn" style="left:67px;top:318px;width:88px;height:26px;line-height:26px">Sing Up</div>
</section>

<!-- Brand header -->
<div class="abs" style="left:640px;top:92px;width:22px;height:22px;border-radius:50%;background:var(--green)"></div>
<div class="abs" style="left:674px;top:78px;font-size:46px;font-weight:400;letter-spacing:2px;color:var(--blue-deep)">BRELL SYSTEMS</div>

<!-- Loading icons -->
<div class="abs" style="left:611px;top:211px;font-size:20px;color:#1f6fb3">Loading Icons</div>
<svg class="abs" style="left:577px;top:251px" width="80" height="80" viewBox="0 0 80 80">
  <circle cx="40" cy="40" r="34" fill="none" stroke="#1e82d0" stroke-width="9" stroke-dasharray="1.6 3.2"/>
  <text x="40" y="47" text-anchor="middle" font-family="Roboto, sans-serif" font-size="19" fill="#1f6fb3">45%</text>
</svg>
<svg class="abs" style="left:685px;top:251px" width="80" height="80" viewBox="0 0 80 80">
  <circle cx="40" cy="40" r="35" fill="#fafafa" stroke="#3b3e45" stroke-width="5"/>
  <circle cx="40" cy="40" r="35" fill="none" stroke="#1e82d0" stroke-width="5" stroke-dasharray="99 220" transform="rotate(-90 40 40)"/>
  <text x="40" y="47" text-anchor="middle" font-family="Roboto, sans-serif" font-size="19" fill="#1f6fb3">45%</text>
</svg>

<!-- Search bar -->
<div class="panel search" style="left:796px;top:260px;width:290px;height:64px;border-radius:4px">
  <div class="glow" style="top:9px"></div>
  <div class="field" style="left:10px;top:17px;width:264px;height:30px;background:linear-gradient(#fff,#d9dde1)">
    <div class="abs" style="left:0;top:0;width:31px;height:30px;background:linear-gradient(#eef3f7,#b8c6d2);border-right:1px solid #9aa7b3"></div>
    <svg class="ico" style="left:7px;top:6px;color:var(--blue-deep)" width="18" height="18"><use href="#i-search"/></svg>
    <span style="margin-left:44px;font-size:13px;color:#6a6e75">Search</span>
  </div>
</div>

<!-- Dashboard (wide) -->
<section class="panel dashboard" style="left:585px;top:366px;width:574px;height:187px">
  <div class="abs" style="left:12px;top:18px;width:34px;height:34px;border-radius:50%;border:2px solid #d8dbe0"></div>
  <svg class="ico" style="left:19px;top:24px" width="20" height="20"><use href="#i-house"/></svg>
  <div class="abs" style="left:56px;top:22px;font-size:20px;font-weight:300">Dashboard</div>
  <div class="vsep" style="left:177px;top:6px;height:62px"></div>
  <div class="cap" style="left:225px;top:17px">HOME</div>
  <div class="cap" style="left:299px;top:17px">NOT HOME</div>
  <div class="toggle" style="left:208px;top:37px;width:160px">
    <div class="fill" style="width:80px"></div>
    <div class="knob" style="left:64px"><svg width="14" height="14" style="color:#fff"><use href="#i-chev-right"/></svg></div>
  </div>
  <div class="vsep" style="left:395px;top:6px;height:62px"></div>
  <div class="abs" style="left:437px;top:12px;font-size:10px;color:#d0d3d8">Notifications Panel</div>
  <svg class="ico" style="left:412px;top:35px" width="24" height="24"><use href="#i-shield"/></svg>
  <svg class="ico" style="left:451px;top:35px" width="24" height="24"><use href="#i-compass"/></svg>
  <svg class="ico" style="left:489px;top:35px" width="26" height="24"><use href="#i-monitor"/></svg>
  <svg class="ico" style="left:528px;top:35px" width="22" height="22"><use href="#i-pen"/></svg>
  <div class="glow" style="top:74px;opacity:.7"></div>
  <div class="abs" style="left:5px;top:64px;width:20px;height:20px;border-radius:50%;border:1.5px solid #d8dbe0"><svg style="position:absolute;left:3px;top:3px;color:#d8dbe0" width="11" height="11"><use href="#i-chev-left"/></svg></div>
  <div class="abs" style="left:550px;top:64px;width:20px;height:20px;border-radius:50%;border:1.5px solid #d8dbe0"><svg style="position:absolute;left:4px;top:3px;color:#d8dbe0" width="11" height="11"><use href="#i-chev-right"/></svg></div>
  <div class="vsep" style="left:123px;top:84px;height:96px"></div>
  <div class="vsep" style="left:269px;top:84px;height:96px"></div>
  <div class="vsep" style="left:421px;top:84px;height:96px"></div>
  <svg class="ico" style="left:20px;top:94px" width="44" height="44"><use href="#i-gear"/></svg>
  <svg class="ico" style="left:62px;top:124px" width="24" height="24" opacity=".6"><use href="#i-gear"/></svg>
  <div class="abs" style="left:21px;top:156px;font-size:19px;font-weight:300">Settings</div>
  <svg class="ico" style="left:170px;top:92px" width="54" height="54"><use href="#i-house"/></svg>
  <div class="abs" style="left:167px;top:156px;font-size:19px;font-weight:300">Houses</div>
  <svg class="ico" style="left:318px;top:94px" width="50" height="50"><use href="#i-door"/></svg>
  <div class="abs" style="left:328px;top:156px;font-size:19px;font-weight:300">Door</div>
  <svg class="ico" style="left:470px;top:92px" width="54" height="54"><use href="#i-shield"/></svg>
  <div class="abs" style="left:462px;top:156px;font-size:19px;font-weight:300">Security</div>
</section>

<!-- Expand marker -->
<div class="abs" style="left:870px;top:533px;width:44px;height:44px;border-radius:50%;background:#fff;border:2px solid #8fd18f;box-shadow:0 2px 4px rgba(0,0,0,.3)">
  <svg class="abs" style="left:8px;top:9px" width="24" height="24" viewBox="0 0 24 24"><path d="M4 7l8 10 8-10" fill="none" stroke="var(--green)" stroke-width="2.2"/></svg>
</div>

<!-- Options (wide) -->
<section class="panel options-wide" style="left:605px;top:571px;width:527px;height:174px;border-radius:8px">
  <div class="abs" style="left:32px;top:8px;font-size:18px;letter-spacing:1px">BRELL</div>
  <div class="abs" style="left:105px;top:8px;font-size:18px;font-weight:300;letter-spacing:.5px">OPTIONS</div>
  <div class="vsep" style="left:305px;top:4px;height:30px"></div>
  <div class="abs" style="left:322px;top:14px;font-size:9px;color:#d0d3d8">NOTIFICATIOS</div>
  <svg class="ico" style="left:402px;top:11px" width="19" height="19"><use href="#i-chat"/></svg>
  <svg class="ico" style="left:430px;top:11px" width="19" height="19"><use href="#i-compass"/></svg>
  <svg class="ico" style="left:457px;top:10px" width="21" height="20"><use href="#i-monitor"/></svg>
  <svg class="ico" style="left:486px;top:11px" width="18" height="18"><use href="#i-pen"/></svg>
  <div class="glow" style="top:38px"></div>
  <div class="vsep" style="left:165px;top:44px;height:122px"></div>
  <div class="vsep" style="left:339px;top:44px;height:122px"></div>
  <div class="abs" style="left:0;top:0;width:165px;height:174px">
    <svg class="ico" style="left:50px;top:54px" width="28" height="28"><use href="#i-gear"/></svg>
    <svg class="ico" style="left:76px;top:74px" width="16" height="16" opacity=".6"><use href="#i-gear"/></svg>
    <div class="cell-label" style="top:94px">Settings</div>
    <div class="lorem" style="left:14px;right:0;top:125px">Lorem ipsum dolor sit amet, consectetur adipisicing elit, sed do eius-mod tempor incididunt</div>
  </div>
  <div class="abs" style="left:170px;top:0;width:169px;height:174px">
    <svg class="ico" style="left:67px;top:56px" width="38" height="34"><use href="#i-monitor"/></svg>
    <div class="cell-label" style="top:94px">Panel Control</div>
    <div class="lorem" style="left:14px;right:10px;top:125px">Lorem ipsum dolor sit amet, consectetur adipisicing elit, sed do eius-mod tempor incididunt</div>
  </div>
  <div class="abs" style="left:344px;top:0;width:183px;height:174px">
    <svg class="ico" style="left:80px;top:52px" width="36" height="34"><use href="#i-card"/></svg>
    <div class="cell-label" style="top:92px">Info</div>
    <div class="lorem" style="left:30px;right:20px;top:120px">Lorem ipsum dolor sit amet, consectetur adipisicing elit, sed do eius-mod tempor incididunt</div>
  </div>
</section>

<!-- Detail view -->
<div class="section-title" style="left:793px;top:778px;font-size:18px">DETAIL VIEW</div>
<section class="abs detail" style="left:582px;top:816px;width:520px;height:270px;border-radius:16px;background:#f4f4f4;border:3px solid #2f3237;box-shadow:0 4px 10px rgba(0,0,0,.35)">
  <div class="abs" style="left:5px;top:5px;width:344px;height:256px;border-radius:12px 0 0 12px;background:linear-gradient(#474b54,#2d3036)"></div>
  <div class="abs" style="left:17px;top:14px;font-size:18px;letter-spacing:1px">BRELL</div>
  <div class="vsep" style="left:90px;top:10px;height:34px"></div>
  <div class="abs" style="left:106px;top:17px;width:20px;height:20px;border-radius:50%;border:1.5px solid #d8dbe0"><svg style="position:absolute;left:3px;top:3px;color:#d8dbe0" width="11" height="11"><use href="#i-chev-left"/></svg></div>
  <div class="abs" style="left:133px;top:12px;font-size:19px;font-weight:300">energy consumer</div>
  <div class="abs" style="left:302px;top:17px;width:20px;height:20px;border-radius:50%;border:1.5px solid #d8dbe0"><svg style="position:absolute;left:4px;top:3px;color:#d8dbe0" width="11" height="11"><use href="#i-chev-right"/></svg></div>
  <div class="sep" style="left:5px;right:171px;top:48px"></div>
  <div class="abs" style="left:15px;top:66px;font-size:9px;color:#d0d3d8">OPTIONS</div>
  <svg class="ico" style="left:25px;top:82px" width="25" height="22"><use href="#i-mail"/></svg>
  <svg class="ico" style="left:25px;top:111px" width="26" height="26"><use href="#i-compass"/></svg>
  <svg class="ico" style="left:25px;top:145px" width="26" height="26"><use href="#i-shield"/></svg>
  <svg class="ico" style="left:23px;top:181px" width="28" height="26"><use href="#i-monitor"/></svg>
  <svg class="ico" style="left:27px;top:214px" width="22" height="22"><use href="#i-pen"/></svg>
  <div class="abs" style="left:15px;top:238px;width:46px;height:1px;background:#6a707a"></div>

  <svg class="abs" style="left:0;top:0" width="350" height="270" viewBox="0 0 350 270">
    <text x="150" y="67" font-family="Roboto, sans-serif" font-size="5" fill="#9aa0a8">Series one</text>
    <rect x="188" y="62" width="15" height="6" fill="#38aef0"/>
    <text x="215" y="67" font-family="Roboto, sans-serif" font-size="5" fill="#9aa0a8">Series two</text>
    <rect x="253" y="62" width="15" height="6" fill="#d7d9dc"/>
    <g stroke="#6e747d" stroke-width=".6">
      <line x1="100" y1="78" x2="100" y2="212"/>
      <line x1="120" y1="78" x2="120" y2="212"/><line x1="136" y1="78" x2="136" y2="212"/><line x1="152" y1="78" x2="152" y2="212"/>
      <line x1="168" y1="78" x2="168" y2="212"/><line x1="184" y1="78" x2="184" y2="212"/><line x1="200" y1="78" x2="200" y2="212"/>
      <line x1="216" y1="78" x2="216" y2="212"/><line x1="232" y1="78" x2="232" y2="212"/><line x1="248" y1="78" x2="248" y2="212"/>
      <line x1="264" y1="78" x2="264" y2="212"/><line x1="280" y1="78" x2="280" y2="212"/><line x1="296" y1="78" x2="296" y2="212"/>
      <line x1="312" y1="78" x2="312" y2="212"/>
    </g>
    <g stroke="#8a9099" stroke-width=".6">
      <line x1="96" y1="85" x2="100" y2="85"/><line x1="96" y1="100" x2="100" y2="100"/><line x1="96" y1="115" x2="100" y2="115"/>
      <line x1="96" y1="130" x2="100" y2="130"/><line x1="96" y1="145" x2="100" y2="145"/><line x1="96" y1="170" x2="100" y2="170"/>
      <line x1="96" y1="185" x2="100" y2="185"/><line x1="96" y1="200" x2="100" y2="200"/>
    </g>
    <path d="M150 155 L156 150 L163 148 L170 146 L176 140 L182 132 L188 138 L194 126 L200 120 L206 128 L212 122 L218 110 L224 118 L230 104 L236 96 L242 104 L248 92 L254 88 L260 102 L264 92 L270 96 L276 116 L282 124 L290 132 L298 142 L306 150 L316 155 Z" fill="#35aaee"/>
    <path d="M103 155 L112 161 L120 166 L128 162 L136 170 L144 176 L152 190 L160 186 L166 176 L172 166 L180 160 L190 156 L190 155 Z" fill="#c9ccd0"/>
    <line x1="100" y1="155" x2="320" y2="155" stroke="#d0d3d8" stroke-width="1"/>
  </svg>

  <svg class="ico" style="left:90px;top:229px" width="16" height="20"><use href="#i-bulb"/></svg>
  <div class="abs" style="left:113px;top:233px;width:30px;height:16px;background:#cfe6f5;border:1px solid #7fb9e0;color:#1f6fb3;font-size:9px;text-align:center;line-height:14px">42%</div>
  <div class="abs" style="left:120px;top:252px;font-size:6px;color:#c4c8ce">DAY</div>
  <svg class="ico" style="left:148px;top:229px" width="16" height="20"><use href="#i-bulb"/></svg>
  <div class="abs" style="left:170px;top:233px;width:36px;height:16px;background:var(--blue);color:#fff;font-size:9px;text-align:center;line-height:16px">58%</div>
  <div class="abs" style="left:177px;top:252px;font-size:6px;color:#c4c8ce">NIGTH</div>
  <div class="abs" style="left:222px;top:224px;font-size:8px;color:#e0e2e6">Information</div>
  <div class="abs" style="left:222px;top:235px;width:60px;font-size:5px;line-height:6px;color:#b9bec5">Daily usage summary for all connected rooms, lamps and devices in the house.</div>
  <div class="abs" style="left:287px;top:224px;width:55px;font-size:5px;line-height:6px;color:#b9bec5">Peak load recorded in the evening hours.</div>

  <nav class="abs" style="left:349px;top:5px;width:164px;height:256px;border-radius:0 12px 12px 0;background:linear-gradient(90deg,#eef1f3,#c4ccd3)">
    <div class="menu-item" style="top:23px">Setup</div>
    <div class="sep" style="top:57px;background:#fff;border-bottom:1px solid #b6bec5"></div>
    <div class="abs" style="left:0;right:0;top:59px;height:43px;background:linear-gradient(#4c5058,#2e3136)"></div>
    <div class="abs" style="left:-8px;top:72px;width:0;height:0;border-top:8px solid transparent;border-bottom:8px solid transparent;border-right:8px solid #35383e"></div>
    <div class="menu-item" style="top:69px;color:#fff">Energy Info</div>
    <div class="menu-item" style="top:117px">Menu</div>
    <div class="sep" style="left:8px;top:150px;background:#fff;border-bottom:1px solid #b6bec5"></div>
    <div class="menu-item" style="top:162px">Turn on/off</div>
    <div class="sep" style="left:8px;top:196px;background:#fff;border-bottom:1px solid #b6bec5"></div>
    <div class="menu-item" style="top:212px">Settings</div>
  </nav>
</section>

<!-- Sidebar navigation -->
<aside class="panel sidebar" style="left:25px;top:415px;width:186px;height:653px;border-radius:10px">
  <div class="abs" style="left:57px;top:12px;width:70px;height:70px;border-radius:50%;border:3px solid #d8dbe0"></div>
  <svg class="ico" style="left:74px;top:28px" width="36" height="36"><use href="#i-house"/></svg>
  <div class="abs" style="left:0;right:0;top:86px;text-align:center;font-size:20px;font-weight:300">Dashboard</div>
  <div class="sep" style="top:118px"></div>
  <div class="cap" style="left:36px;top:137px;font-size:10px">HOME</div>
  <div class="cap" style="left:101px;top:137px;font-size:10px">NOT HOME</div>
  <div class="toggle" style="left:19px;top:155px;width:143px">
    <div class="fill" style="width:72px"></div>
    <div class="knob" style="left:55px"><svg width="14" height="14" style="color:#fff"><use href="#i-chev-right"/></svg></div>
  </div>
  <div class="sep" style="top:184px"></div>
  <svg class="ico" style="left:37px;top:206px" width="22" height="24"><use href="#i-bulb"/></svg>
  <div class="row-label" style="top:208px">Light</div>
  <div class="sep" style="top:251px"></div>
  <svg class="ico" style="left:35px;top:272px" width="26" height="26"><use href="#i-user"/></svg>
  <div class="row-label" style="top:276px;left:91px">Users</div>
  <div class="row-active" style="top:319px;height:68px"></div>
  <svg class="ico" style="left:35px;top:340px;color:#2f3237" width="26" height="28"><use href="#i-shield"/></svg>
  <div class="row-label" style="top:340px;color:var(--blue-deep);font-weight:400">Security</div>
  <svg class="ico" style="left:36px;top:407px" width="26" height="26"><use href="#i-door"/></svg>
  <div class="row-label" style="top:407px;left:89px">Door</div>
  <div class="sep" style="top:456px"></div>
  <svg class="ico" style="left:33px;top:479px" width="26" height="26"><use href="#i-house"/></svg>
  <div class="row-label" style="top:480px">Houses</div>
  <div class="sep" style="top:525px"></div>
  <svg class="ico" style="left:30px;top:546px" width="22" height="22"><use href="#i-gear"/></svg>
  <svg class="ico" style="left:47px;top:558px" width="12" height="12" opacity=".6"><use href="#i-gear"/></svg>
  <div class="row-label" style="top:548px">Settings</div>
  <div class="sep" style="top:592px"></div>
  <div class="abs" style="left:0;right:0;top:600px;text-align:center;font-size:10px;color:#d0d3d8">Notifications Panel</div>
  <svg class="ico" style="left:20px;top:618px" width="26" height="26"><use href="#i-shield"/></svg>
  <svg class="ico" style="left:62px;top:618px" width="26" height="26"><use href="#i-compass"/></svg>
  <svg class="ico" style="left:100px;top:618px" width="28" height="26"><use href="#i-monitor"/></svg>
  <svg class="ico" style="left:140px;top:621px" width="22" height="22"><use href="#i-pen"/></svg>
</aside>

<!-- Options column -->
<aside class="panel options-column" style="left:231px;top:516px;width:167px;height:516px;border-radius:10px">
  <div class="abs" style="left:0;right:0;top:14px;text-align:center;font-size:19px;font-weight:300;letter-spacing:.5px">OPTIONS</div>
  <div class="glow" style="top:48px"></div>
  <svg class="ico" style="left:55px;top:66px" width="28" height="28"><use href="#i-gear"/></svg>
  <svg class="ico" style="left:79px;top:86px" width="15" height="15" opacity=".6"><use href="#i-gear"/></svg>
  <div class="cell-label" style="top:106px">Settings</div>
  <div class="lorem" style="left:12px;right:12px;top:138px">Lorem ipsum dolor sit amet, consectetur adipisicing elit, sed do eius-mod tempor incididunt</div>
  <div class="glow" style="top:181px"></div>
  <div class="row-active" style="top:186px;height:126px"></div>
  <svg class="ico" style="left:67px;top:200px;color:#3a3d44" width="36" height="32"><use href="#i-monitor"/></svg>
  <div class="cell-label" style="top:236px;color:var(--blue-deep);font-weight:400">Panel Control</div>
  <div class="lorem" style="left:12px;right:12px;top:268px;color:#5b6068">Lorem ipsum dolor sit amet, consectetur adipisicing elit, sed do eius-mod tempor incididunt</div>
  <div class="glow" style="top:312px"></div>
  <svg class="ico" style="left:64px;top:326px" width="36" height="32"><use href="#i-card"/></svg>
  <div class="cell-label" style="top:364px">Info</div>
  <div class="lorem" style="left:12px;right:12px;top:393px">Lorem ipsum dolor sit amet, consectetur adipisicing elit, sed do eius-mod tempor incididunt</div>
  <div class="sep" style="top:436px"></div>
  <div class="abs" style="left:0;right:0;top:448px;text-align:center;font-size:10px;color:#d0d3d8">NOTIFICATIONS</div>
  <svg class="ico" style="left:10px;top:473px" width="26" height="24"><use href="#i-chat"/></svg>
  <svg class="ico" style="left:48px;top:472px" width="26" height="26"><use href="#i-compass"/></svg>
  <svg class="ico" style="left:90px;top:471px" width="28" height="26"><use href="#i-monitor"/></svg>
  <svg class="ico" style="left:137px;top:475px" width="20" height="20"><use href="#i-pen"/></svg>
</aside>

</body>
</html>
```